Lawn Sign For Construction Projects - Vantor Power

This contest is for a lawn sign that will be placed in the front yard of recently completed construction projects. The goal here is to have a bold advertising sign that is visible from a vehicle driving past.

We are still deciding on the default size for our sign, we also may use multiple sizes. The two sizes we will more than likely be using are: 18"h x 24"w and 24"h x 36"w.

Preference will be given to designers that submit original designs that tie into our current brand and are either in both the size formats listed above or are easy to scale in photoshop or illustrator.

In the files, you will see our logo and an example of a lawn sign.

Please contact us with any questions or comments you may have!

Thank You,
- The Vantor Power Team

Industry/Entity Type

Residential Construction

Colors
34a7d8
ffffff
faa54b

Requirements
Nice to have
• 1. The sign must tie into our current branding and color scheme.
• 2. The sign must be clearly visible and readable.
• 3. The sign must include our phone number in readable print.
• 4. Our website written in small print along the bottom of the sign.
• 5. Must mention we install the following products:
• a.) Solar
• b.) Roofing
• c.) Windows
• d.) Artificial Lawn
• e.) Whole House Fans
• f.) Patio Covers

```html
<!DOCTYPE html>
<html lang="en">
<head>
<meta charset="UTF-8">
<title>Vantor Power – Lawn Sign</title>
<link href="https://fonts.googleapis.com/css2?family=Montserrat:wght@600&family=Roboto:wght@300;400;700&display=swap" rel="stylesheet">
<style>
  :root {
    --brand-blue: #1377bd;
    --brand-orange: #ee7623;
    --sign-white: #ffffff;
  }
  * { margin: 0; padding: 0; box-sizing: border-box; }
  html, body {
    width: 1200px;
    height: 1000px;
    overflow: hidden;
    background: var(--brand-blue);
  }
  .lawn-sign {
    position: relative;
    width: 1200px;
    height: 1000px;
    background: var(--brand-blue);
    color: var(--sign-white);
    font-family: "Roboto", Arial, sans-serif;
  }
  .brand-circle {
    position: absolute;
    left: 452px;
    top: 27px;
    width: 296px;
    height: 296px;
  }
  .brand-name {
    position: absolute;
    top: 358px;
    left: 0;
    width: 100%;
    text-align: center;
    font-family: "Montserrat", Arial, sans-serif;
    font-weight: 600;
    font-size: 94px;
    line-height: 1;
    letter-spacing: 1px;
    color: var(--sign-white);
  }
  .phone-number {
    position: absolute;
    top: 478px;
    left: 0;
    width: 100%;
    text-align: center;
    font-weight: 300;
    font-size: 106px;
    line-height: 1;
    letter-spacing: 1px;
  }
  .services-band {
    position: absolute;
    top: 598px;
    left: 2px;
    width: 1198px;
    height: 232px;
    background: var(--brand-orange);
    display: flex;
    flex-direction: column;
    justify-content: center;
    align-items: center;
    gap: 6px;
  }
  .service-line {
    font-weight: 700;
    font-size: 55px;
    line-height: 57px;
    white-space: nowrap;
    text-transform: uppercase;
  }
  .website {
    position: absolute;
    top: 860px;
    left: 0;
    width: 100%;
    text-align: center;
    font-weight: 400;
    font-size: 96px;
    line-height: 1;
    letter-spacing: 1px;
  }
</style>
</head>
<body>
  <main class="lawn-sign">
    <svg class="brand-circle" viewBox="0 0 296 296" aria-hidden="true">
      <circle cx="148" cy="148" r="139" fill="none" stroke="var(--brand-orange)" stroke-width="18"/>
    </svg>

    <h1 class="brand-name">VANTOR POWER</h1>

    <p class="phone-number">555-555-5555</p>

    <section class="services-band" aria-label="Services we install">
      <p class="service-line">Solar - Roofing - Windows</p>
      <p class="service-line">Artificial Lawn - Whole House Fans</p>
      <p class="service-line">Patio Covers</p>
    </section>

    <p class="website">websitehere.com</p>
  </main>
</body>
</html>
```